RK Cooling (logo) - Celebrating 55 Years Servicing the Chicago Suburbs. Summer is Almost Here! Make sure your system is running properly and efficiently. The industry standard recommends an A/C Clean & Check once a year.
A/C Clean & Check
Regular Preventive Maintenance Can:
-Help Prolong the Life of your Equipment
-Help Lower Your Monthly Energy Costs
-Save Costs on Future Repairs

Mention this Postcard and Take $10.00 Off
Call (555) 318-4062 I Address: 87 Birchwood Ave. Lemont, IL
_______________________________________________
BACK SIDE:
Proudly Serving Chicagoland Area Since 1961- We Also Service and Sell:
-Northfield Premier Equipment.
-Brightvale Air Cleaners & Humidifier Systems.
-Hot Water Heaters, Boilers, and Digital Thermostats.
-Residential and Commercial Fabrication. Custom Welding.

Schedule Your Spring Clean & Check Today
Phone: (555) 318-4062
Mail: rkcooling@mailbox-example.net
Website: www.rkcoolingservice-example.com

I had pixel hive make a Fall Clean and Check (for furnaces) in September of 2015. Feel free too look back for ideas. The postcard needs to be creative and not the same as the fall one! Added Tuesday, March 29, 2016

Target Market(s)

HVAC Industry, Residential

Industry/Entity Type

Air Conditioning

Colors
0255a3
f6faec

Requirements
Must have
• The following text in the project description. Feel free to add more.
Nice to have
• One small picture or clipart on the front. Maybe a picture of something summery or an air conditioner.
Should not have
• No spelling mistakes. Nothing too basic.

```html
<!DOCTYPE html>
<html lang="en">
<head>
<meta charset="utf-8">
<title>RK Cooling – Summer Clean &amp; Check Postcard</title>
<link rel="stylesheet" href="https://fonts.googleapis.com/css2?family=Oswald:wght@400;500&family=Roboto+Condensed:wght@400;700&family=Lato:ital,wght@0,700;0,900;1,700;1,900&display=swap">
<style>
  :root {
    --navy: #2e3192;
    --navy-dark: #1f2170;
    --red: #e21b23;
    --ink: #1d1d1f;
    --paper: #ffffff;
    --stage: #e9ebee;
    --rule: #b9bcc2;
  }
  * { box-sizing: border-box; margin: 0; padding: 0; }
  html, body { width: 902px; height: 1200px; overflow: hidden; }
  body { background: var(--stage); font-family: "Lato", sans-serif; color: var(--ink); position: relative; }

  .postcard { position: absolute; left: 131px; width: 640px; height: 500px; background: var(--paper); overflow: hidden; box-shadow: 0 4px 14px rgba(0,0,0,.18); }
  .postcard--front { top: 45px; }
  .postcard--back { top: 640px; }
  .postcard svg.shapes { position: absolute; inset: 0; }
  .abs { position: absolute; }

  /* front */
  .brand { left: 22px; top: 34px; display: flex; align-items: center; gap: 7px; font-family: "Lato", sans-serif; font-weight: 900; font-size: 25px; color: var(--navy); }
  .brand-dot { width: 12px; height: 12px; border-radius: 50%; background: var(--navy); }
  .headline { left: 242px; top: 24px; width: 390px; }
  .headline-kicker { font-family: "Oswald", sans-serif; font-weight: 500; font-size: 27px; line-height: 1.05; color: var(--red); letter-spacing: -.2px; }
  .headline-main { font-family: "Lato", sans-serif; font-weight: 900; font-size: 28.5px; line-height: 1.15; color: var(--navy); }
  .season { font-family: "Roboto Condensed", sans-serif; font-size: 27px; color: var(--navy); margin-top: 6px; }
  .intro { font-style: italic; font-weight: 900; font-size: 13.6px; line-height: 1.3; margin-top: 6px; color: var(--ink); }
  .service-list { list-style: none; margin-top: 10px; margin-left: 2px; }
  .service-list li { font-weight: 900; font-size: 12px; margin-bottom: 8px; display: flex; align-items: center; gap: 10px; }
  .service-list li::before { content: ""; width: 8px; height: 8px; border-radius: 50%; background: var(--navy); }
  .benefit-list { list-style: none; margin-left: 26px; margin-top: -1px; }
  .benefit-list li { font-style: italic; font-weight: 700; font-size: 10.5px; margin-bottom: 5px; display: flex; align-items: center; gap: 7px; }
  .benefit-list svg { width: 9px; height: 9px; }

  .contact-front { left: 32px; top: 418px; color: #fff; font-family: "Roboto Condensed", sans-serif; font-size: 16px; }
  .contact-front p { display: flex; align-items: center; gap: 9px; margin-bottom: 10px; }
  .contact-front svg { width: 14px; height: 14px; }

  .offer { left: 236px; top: 358px; width: 146px; height: 146px; border-radius: 50%; background: radial-gradient(circle at 50% 35%, #fff 0%, #f1f1f3 55%, #c9cbd0 100%); border: 4px solid var(--navy); text-align: center; padding-top: 22px; }
  .offer-line { font-family: "Roboto Condensed", sans-serif; color: var(--navy); font-size: 17px; line-height: 1.02; }
  .offer-line--small { font-size: 15px; }
  .offer-amount { font-family: "Oswald", sans-serif; font-weight: 500; color: var(--red); font-size: 27px; display: inline-flex; align-items: center; gap: 3px; margin-top: 1px; }
  .offer-amount small { font-size: 11px; writing-mode: vertical-rl; color: var(--navy-dark); }

  /* back */
  .back-header { left: 0; top: 0; width: 330px; height: 90px; text-align: center; padding-top: 24px; }
  .back-header p { font-family: "Oswald", sans-serif; color: #fff; font-size: 15px; letter-spacing: .1px; }
  .back-header strong { display: block; font-family: "Oswald", sans-serif; font-weight: 400; color: var(--red); font-size: 27px; line-height: 1.2; }
  .sell-tag { left: 0; top: 102px; width: 260px; height: 30px; background: var(--red); border-radius: 0 15px 15px 0; color: #fff; font-family: "Roboto Condensed", sans-serif; font-size: 20px; padding-left: 20px; line-height: 30px; }
  .sell-list { left: 22px; top: 143px; width: 300px; list-style: none; }
  .sell-list li { font-style: italic; font-weight: 700; font-size: 13px; line-height: 1.3; margin-bottom: 9px; padding-left: 16px; position: relative; }
  .sell-list li::before { content: ""; position: absolute; left: 0; top: 6px; width: 6px; height: 6px; border-radius: 50%; background: var(--navy); }
  .schedule { left: 18px; top: 300px; font-style: italic; font-weight: 900; font-size: 14.5px; color: var(--red); }
  .contact-back { left: 20px; top: 345px; color: #fff; font-weight: 700; font-size: 11.5px; }
  .contact-back p { display: flex; align-items: center; gap: 10px; margin-bottom: 8px; }
  .contact-back svg { width: 10px; height: 10px; }
  .stamp-box { left: 500px; top: 43px; width: 110px; height: 110px; border: 1px solid #8a8d93; }
  .address-line { left: 373px; width: 240px; height: 1px; background: var(--rule); }
</style>
</head>
<body>

<!-- FRONT -->
<section class="postcard postcard--front">
  <svg class="shapes" width="640" height="500" viewBox="0 0 640 500">
    <defs>
      <linearGradient id="portraitTone" x1="0" y1="0" x2="1" y2="1">
        <stop offset="0" stop-color="#f3eee9"/><stop offset=".55" stop-color="#dcc7b8"/><stop offset="1" stop-color="#eef0f4"/>
      </linearGradient>
      <linearGradient id="techTone" x1="0" y1="0" x2="1" y2="1">
        <stop offset="0" stop-color="#c9d3df"/><stop offset=".5" stop-color="#5b6b80"/><stop offset="1" stop-color="#2a3142"/>
      </linearGradient>
      <linearGradient id="bandTone" x1="0" y1="0" x2="1" y2="0">
        <stop offset="0" stop-color="#2e3192"/><stop offset="1" stop-color="#3a3fa8"/>
      </linearGradient>
    </defs>
    <!-- portrait area -->
    <rect role="img" aria-label="Photo of a young woman wiping her brow with a towel on a hot day" x="0" y="120" width="240" height="240" fill="url(#portraitTone)"/>
    <!-- top swoosh -->
    <path d="M0,118 Q190,110 236,0 L258,0 Q220,130 0,136 Z" fill="var(--navy)"/>
    <path d="M0,112 Q180,104 226,0 L240,0 Q200,118 0,124 Z" fill="var(--red)"/>
    <!-- bottom band -->
    <path d="M0,300 Q220,380 640,420 L640,500 L0,500 Z" fill="var(--red)"/>
    <path d="M0,312 Q220,392 640,432 L640,500 L0,500 Z" fill="#fff"/>
    <path d="M0,322 Q220,402 640,442 L640,500 L0,500 Z" fill="url(#bandTone)"/>
    <!-- technician photo -->
    <path d="M636,268 Q520,250 450,330 Q425,370 425,430 L425,500 L640,500 L640,268 Z" fill="var(--red)"/>
    <path role="img" aria-label="Photo of a technician in a hard hat servicing an air conditioning unit" d="M640,282 Q530,266 466,338 Q440,375 440,430 L440,500 L640,500 Z" fill="url(#techTone)"/>
    <path d="M640,255 Q560,240 510,270" stroke="var(--navy)" stroke-width="8" fill="none"/>
  </svg>

  <div class="abs brand"><span class="brand-dot"></span>RK Cooling</div>

  <div class="abs headline">
    <h1 class="headline-kicker">CELEBRATING 55 YEARS SERVICING</h1>
    <h2 class="headline-main">THE CHICAGO SUBURBS</h2>
    <p class="season">Summer is Almost Here!</p>
    <p class="intro">Make sure your system is running properly and efficiently. The industry standard recommends an A/C Clean &amp; Check once a year.</p>
    <ul class="service-list">
      <li>A/C Clean &amp; Check</li>
      <li>Regular Preventive Maintenance Can:</li>
    </ul>
    <ul class="benefit-list">
      <li><svg viewBox="0 0 10 10"><path d="M1,5 L4,8 L9,1" stroke="var(--navy)" stroke-width="2" fill="none"/></svg>Help Prolong the Life of your Equipment</li>
      <li><svg viewBox="0 0 10 10"><path d="M1,5 L4,8 L9,1" stroke="var(--navy)" stroke-width="2" fill="none"/></svg>Help Lower Your Monthly Energy Costs</li>
      <li><svg viewBox="0 0 10 10"><path d="M1,5 L4,8 L9,1" stroke="var(--navy)" stroke-width="2" fill="none"/></svg>Save Costs on Future Repairs</li>
    </ul>
  </div>

  <div class="abs contact-front">
    <p><svg viewBox="0 0 14 14"><path d="M3,1 L5,1 L6,4 L4.5,5 Q6,8.5 9,9.5 L10,8 L13,9 L13,11 Q12,13 10,13 Q2,11 1,3 Q1,1 3,1 Z" fill="var(--red)"/></svg>(555) 318-4062</p>
    <p><svg viewBox="0 0 14 14"><path d="M7,1 L13,7 L11,7 L11,13 L8.5,13 L8.5,9 L5.5,9 L5.5,13 L3,13 L3,7 L1,7 Z" fill="var(--red)"/></svg>87 Birchwood Ave. Lemont, IL</p>
  </div>

  <div class="abs offer">
    <p class="offer-line">MENTION THIS</p>
    <p class="offer-line">POSTCARD</p>
    <p class="offer-line offer-line--small">&amp; Take</p>
    <p class="offer-amount">$10.00<small>Off</small></p>
  </div>
</section>

<!-- BACK -->
<section class="postcard postcard--back">
  <svg class="shapes" width="640" height="500" viewBox="0 0 640 500">
    <defs>
      <linearGradient id="panelTone" x1="0" y1="0" x2="1" y2="0">
        <stop offset="0" stop-color="#2e3192"/><stop offset="1" stop-color="#4b50b5"/>
      </linearGradient>
    </defs>
    <rect x="0" y="0" width="300" height="90" fill="url(#panelTone)"/>
    <rect x="0" y="335" width="300" height="75" fill="url(#panelTone)"/>
    <path d="M300,0 L340,0 Q355,60 350,200 Q345,330 330,410 L300,410 L300,335 L300,90 Z" fill="#fff"/>
    <path d="M300,0 Q335,10 326,90 L300,90 Z" fill="url(#panelTone)"/>
    <path d="M300,335 L324,335 Q322,380 316,410 L300,410 Z" fill="url(#panelTone)"/>
    <path d="M305,0 Q345,120 328,410" stroke="var(--red)" stroke-width="9" fill="none"/>
    <path d="M326,60 Q356,220 336,410" stroke="var(--ink)" stroke-width="5" fill="none"/>
  </svg>

  <div class="abs back-header">
    <p>PROUDLY SERVING CHICAGOLAND AREA</p>
    <strong>SINCE 1961</strong>
  </div>

  <div class="abs sell-tag">We Also Service and Sell:</div>

  <ul class="abs sell-list">
    <li>Northfield Premier Equipment</li>
    <li>Brightvale Air Cleaners &amp; Humidifier Systems</li>
    <li>Hot Water Heaters, Boilers, and Digital Thermostats</li>
    <li>Residential and Commercial Fabrication</li>
    <li>Custom Welding</li>
  </ul>

  <p class="abs schedule">Schedule Your Spring Clean &amp; Check Today</p>

  <div class="abs contact-back">
    <p><svg viewBox="0 0 14 14"><path d="M3,1 L5,1 L6,4 L4.5,5 Q6,8.5 9,9.5 L10,8 L13,9 L13,11 Q12,13 10,13 Q2,11 1,3 Q1,1 3,1 Z" fill="var(--red)"/></svg>(555) 318-4062</p>
    <p><svg viewBox="0 0 14 14"><rect x="1" y="3" width="12" height="8" fill="var(--red)"/><path d="M1,3 L7,8 L13,3" stroke="#fff" stroke-width="1.2" fill="none"/></svg>rkcooling@mailbox-example.net</p>
    <p><svg viewBox="0 0 14 14"><circle cx="7" cy="7" r="6" fill="var(--red)"/><path d="M1,7 H13 M7,1 Q3,7 7,13 M7,1 Q11,7 7,13" stroke="#fff" stroke-width=".9" fill="none"/></svg>www.rkcoolingservice-example.com</p>
  </div>

  <div class="abs stamp-box"></div>
  <div class="abs address-line" style="top:230px"></div>
  <div class="abs address-line" style="top:273px"></div>
  <div class="abs address-line" style="top:318px"></div>
</section>

</body>
</html>
```